KPT Building And Maintenance

Need a very professional looking double sided Buisiness card with all my details phone number, name, email, license number.

Target Market(s)

construction industry

Industry/Entity Type

building

Contact Information for Business Card

Name Dale Whitcombe. Email Address Info@KPTBuilding.example.au mobile number 0452918730 licence number 871406D. web site

```html
<!DOCTYPE html>
<html lang="en">
<head>
<meta charset="utf-8">
<title>KPT Building And Maintenance – Business Card</title>
<link href="https://fonts.googleapis.com/css2?family=Montserrat:wght@400;500;700&display=swap" rel="stylesheet">
<style>
  :root {
    --stage: #3a3a3a;
    --card-light: #ffffff;
    --card-dark: #141414;
    --brand-blue: #1f8fd6;
    --text-grey: #6b6b6b;
    --text-white: #ffffff;
  }
  * { box-sizing: border-box; margin: 0; padding: 0; }
  html, body {
    width: 1200px; height: 801px; overflow: hidden;
    background: var(--stage);
    font-family: "Montserrat", Arial, sans-serif;
  }
  .stage {
    width: 1200px; height: 801px;
    display: flex; align-items: center; justify-content: center; gap: 40px;
  }
  .card {
    width: 520px; height: 297px;
    flex: 0 0 520px;
    position: relative;
    display: flex; align-items: center; justify-content: center;
    overflow: hidden;
    box-shadow: 0 10px 30px rgba(0,0,0,.35);
  }
  .card--front { background: var(--card-light); border-bottom: 4px solid var(--brand-blue); padding: 0 24px; }
  .card--back { background: var(--card-dark); gap: 30px; border-bottom: 2px solid var(--brand-blue); padding: 0 24px; }

  .holder { flex: 0 0 auto; text-align: right; }
  .holder__name {
    color: var(--brand-blue); font-weight: 700; font-size: 19px; letter-spacing: .2px;
    text-transform: uppercase; white-space: nowrap;
  }
  .holder__licence { color: var(--text-grey); font-size: 12.5px; margin-top: 4px; white-space: nowrap; }

  .divider { display: block; flex: 0 0 1px; width: 1px; background: var(--brand-blue); }
  .card--front .divider { height: 62px; margin: 0 18px; }
  .card--back .divider { height: 120px; }

  .contact { list-style: none; display: flex; flex-direction: column; gap: 6px; flex: 0 0 auto; }
  .contact__item {
    display: flex; align-items: center; gap: 7px;
    color: var(--text-grey); font-size: 11.5px; white-space: nowrap;
  }
  .contact__icon { width: 10px; height: 10px; fill: var(--brand-blue); flex: 0 0 auto; }

  .brand-name {
    color: var(--text-white); font-weight: 700; text-transform: uppercase;
    line-height: 1.15; text-align: center; letter-spacing: 1px;
  }
  .brand-name--short { font-size: 28px; white-space: nowrap; }
  .brand-name--full { font-size: 16px; max-width: 180px; }
</style>
</head>
<body>
<main class="stage">
  <section class="card card--front" aria-label="Business card front">
    <div class="holder">
      <p class="holder__name">Dale Whitcombe</p>
      <p class="holder__licence">licence number 871406D</p>
    </div>
    <span class="divider"></span>
    <ul class="contact">
      <li class="contact__item">
        <svg class="contact__icon" viewBox="0 0 24 24" aria-hidden="true"><path d="M6.6 10.8a15.1 15.1 0 0 0 6.6 6.6l2.2-2.2a1 1 0 0 1 1-.25 11.4 11.4 0 0 0 3.6.57 1 1 0 0 1 1 1V20a1 1 0 0 1-1 1A17 17 0 0 1 3 4a1 1 0 0 1 1-1h3.5a1 1 0 0 1 1 1c0 1.25.2 2.45.57 3.57a1 1 0 0 1-.25 1z"/></svg>
        0452918730
      </li>
      <li class="contact__item">
        <svg class="contact__icon" viewBox="0 0 24 24" aria-hidden="true"><path d="M2 5h20v14H2zm2 2v.5l8 5 8-5V7l-8 5z"/></svg>
        Info@KPTBuilding.example.au
      </li>
      <li class="contact__item">
        <svg class="contact__icon" viewBox="0 0 24 24" aria-hidden="true"><circle cx="12" cy="12" r="10"/></svg>
        www.KPTBuilding.example.au
      </li>
    </ul>
  </section>

  <section class="card card--back" aria-label="Business card back">
    <p class="brand-name brand-name--short">KPT Building</p>
    <span class="divider"></span>
    <p class="brand-name brand-name--full">KPT Building And Maintenance</p>
  </section>
</main>
</body>
</html>
```